Business card design needed

I would like a one sided black business card with the information provided above. Refer to my website www.lobcrafttennis.com.au for an example of colors I have used for my site, would like to keep this consistent for my business cards also, I will upload my logo below.

I am a new small business that provides tennis customers with racquet re stringing, tennis strings and accessories.

Industry/Entity Type

Small Business

Contact Information for Business Card

Lob Craft Tennis

Dennis Morrow
Managing Director

lobcrafttennis@mailbay.com
www.lobcrafttennis.com.au
0412 695 203

Racquet Restringing/Tennis Strings/Accessories

Requirements
Must have
• Must have my logo and card must be black

```html
<!DOCTYPE html>
<html lang="en">
<head>
<meta charset="utf-8">
<title>Lob Craft Tennis – Business Card</title>
<link rel="stylesheet" href="https://fonts.googleapis.com/css2?family=PT+Sans:ital,wght@0,400;0,700;1,700&display=swap">
<style>
  :root {
    --backdrop: #d9d6d2;
    --card-black: #030505;
    --lime: #b5d334;
    --court-blue: #1f5a8c;
    --white: #ffffff;
  }
  html, body {
    margin: 0;
    width: 1200px;
    height: 750px;
    overflow: hidden;
    background: var(--backdrop);
    font-family: "PT Sans", Arial, sans-serif;
  }
  .card {
    position: absolute;
    left: 75px;
    top: 75px;
    width: 1050px;
    height: 598px;
    border-radius: 30px;
    overflow: hidden;
    background: var(--card-black);
  }
  .card-shapes {
    position: absolute;
    inset: 0;
  }
  .brand {
    position: absolute;
    left: 55px;
    top: 118px;
    display: flex;
    align-items: center;
    gap: 16px;
  }
  .brand-dot {
    width: 42px;
    height: 42px;
    border-radius: 50%;
    background: var(--lime);
  }
  .brand-name {
    margin: 0;
    font-size: 52px;
    font-weight: 700;
    color: var(--lime);
    letter-spacing: 0.5px;
    line-height: 1;
  }
  .contact {
    position: absolute;
    left: 45px;
    top: 386px;
    color: var(--white);
  }
  .contact-name {
    margin: 0 0 6px;
    color: var(--lime);
    font-size: 33px;
    font-weight: 700;
    line-height: 1.2;
  }
  .contact-role {
    font-size: 26px;
    font-weight: 400;
  }
  .contact-line {
    margin: 0;
    font-size: 26px;
    line-height: 44px;
  }
  .contact-label {
    font-weight: 700;
    font-style: italic;
  }
</style>
</head>
<body>
  <div class="card">
    <svg class="card-shapes" width="1050" height="598" viewBox="0 0 1050 598" aria-hidden="true">
      <path class="green-band" fill="var(--lime)"
            d="M838,0 L1050,0 L1050,598 L828,598 C900,560 965,460 975,330 C985,200 940,80 838,0 Z"/>
      <path class="blue-swoosh" fill="var(--court-blue)"
            d="M570,598 C760,545 920,430 967,225 C975,380 915,525 815,598 Z"/>
    </svg>

    <div class="brand">
      <span class="brand-dot"></span>
      <h1 class="brand-name">Lob Craft Tennis</h1>
    </div>

    <div class="contact">
      <p class="contact-name">Dennis Morrow - <span class="contact-role">Managing Director</span></p>
      <p class="contact-line"><span class="contact-label">phone</span> 0412 695 203</p>
      <p class="contact-line"><span class="contact-label">email</span> lobcrafttennis@mailbay.com</p>
      <p class="contact-line"><span class="contact-label">web</span> www.lobcrafttennis.com.au</p>
    </div>
  </div>
</body>
</html>
```